Groovy little Insurance brokerage needs a new look

We have a new logo, but need to work out how to make it work for us!
We are a small insurance broking firm (three staff with different focus and styles), with lots of energy, experience and enthusiasm. A focus on both commercial and domestic market. We would like our cards to show a fresh look - while veering away from the 'run of the mill' insurance industry (often dull) approach.
Updates

Thanks to all for your concepts.

Had some great ideas come back, now just the process of picking which one is going to work best for us...
Will advise when we've had an opportunity to review.

Thanks!
From the team at
Kestrel Dunmore Insurance Brokers

Thanks SO much to all of your for your great designs.  Now just a process of sorting out the favorites.  If yours is eliminated, just want to say a collective thank you for your efforts!

Industry/Entity Type

Business

```html
<!DOCTYPE html>
<html lang="en">
<head>
<meta charset="utf-8">
<title>Kestrel Dunmore Insurance Brokers – Business Card</title>
<link href="https://fonts.googleapis.com/css2?family=Raleway:wght@300;400;600&display=swap" rel="stylesheet">
<style>
  :root {
    --page-bg: #ecebe8;
    --card-bg: #ffffff;
    --teal: #16a8c0;
    --teal-light: #8fd4e2;
    --mark-tint: #a9dbe6;
    --ink-dark: #3b3b3d;
    --ink-grey: #6d6f72;
  }
  * { box-sizing: border-box; margin: 0; padding: 0; }
  html, body {
    width: 1200px; height: 1184px; overflow: hidden;
    background: var(--page-bg);
    font-family: "Raleway", sans-serif;
  }
  .card {
    position: absolute; left: 75px; top: 292px;
    width: 1050px; height: 600px;
    background: var(--card-bg);
    box-shadow: 0 10px 30px rgba(0,0,0,0.12);
    overflow: hidden;
  }
  .card-band { position: absolute; inset: 0; }
  .brand {
    position: absolute; left: 300px; top: 78px;
    display: flex; align-items: center; gap: 26px;
  }
  .brand-square { width: 90px; height: 90px; background: var(--mark-tint); }
  .brand-name {
    font-weight: 600; font-size: 34px; line-height: 1.15;
    color: var(--ink-dark); width: 400px;
  }
  .person { position: absolute; left: 350px; top: 300px; }
  .person-name {
    font-size: 40px; font-weight: 400; letter-spacing: 0.5px;
    color: var(--teal); white-space: nowrap;
  }
  .person-name .surname { color: var(--teal-light); }
  .person-title {
    margin-top: 4px; font-size: 18px; font-weight: 400;
    letter-spacing: 12px; color: var(--ink-grey);
  }
  .contact { position: absolute; left: 720px; top: 235px; color: var(--ink-grey); }
  .address { font-size: 20px; line-height: 1.45; font-weight: 300; }
  .lines { margin-top: 60px; font-size: 20px; font-weight: 300; }
  .lines li { list-style: none; display: flex; gap: 18px; margin-bottom: 16px; }
  .lines .label { font-weight: 600; color: var(--ink-dark); width: 20px; }
</style>
</head>
<body>
  <div class="card">
    <svg class="card-band" viewBox="0 0 1050 600" width="1050" height="600" aria-hidden="true">
      <path d="M0 0 H180 Q250 320 420 600 H0 Z" fill="var(--teal)"/>
    </svg>

    <div class="brand">
      <div class="brand-square"></div>
      <div class="brand-name">Kestrel Dunmore Insurance Brokers</div>
    </div>

    <div class="person">
      <div class="person-name">NAME<span class="surname">SURNAME</span></div>
      <div class="person-title">TITLE</div>
    </div>

    <div class="contact">
      <p class="address">42 Harbour Lane,<br>Ste 3, Fernvale, FL 1720</p>
      <ul class="lines">
        <li><span class="label">T</span>+2 555-010-204</li>
        <li><span class="label">M</span>+2 555-010-205</li>
        <li><span class="label">F</span>+2 555-010-206</li>
        <li><span class="label">E</span>name@kestreldunmore.com</li>
      </ul>
    </div>
  </div>
</body>
</html>
```